BRIX Rentals ( Website Graphic design ) small property management new business ( real estate )

I need a website designed for a new small Property Management ( no sales ) company I'm starting up soon. I have a design in mind that I like and would like to keep it quite similar to this if possible using my logo and colour scheme and slightly ALTER the layout. and maybe a little more interactive with some motion and images etc
Please see the link to show the simplicity I'm after. I want to be bold ad very clear and concise. I love the simplicity of this design but not necessarily the pages with just text on them. I would want them to be a bit more interesting with some pictures and photos. http://www.lindavostrel.com.au/

The branding on the site should be bold and very sharp.

My target market is the mid to high end of the rental market in Darwin Australia and should reflect "good quality, outstanding service and attention to detail, energetic, integrity, "

I will only require a few pages to start with, Home / Company Profile / Management Services / Owners information / Tenant information / Properties and About Darwin. I will be able to provide text for each of the pages but would be no more than 4-6 paragraphs apart from the management services page which would detail a number of the services we would offer. The properties page will just be a link to homelistz,com.au to show my listings and then a couple more links to owner and tenant portals, chatterbox page etc. It must also be responsive to mobile devices.

I would also like to include a chatterbox page design and build.

regards
Marta Penhale

Target Market(s)

property owners, investors, Darwin Australia, renters, ages 30 - 60, tenants

Industry/Entity Type

Property Management

Font styles to use
Other font styles liked:
• i like helvetica, but not essential

Requirements
Must have
• Clean and crisp pages, not busy , responsive to devices
• links to portals and chatterbox, any ability to add other links at a later date.
Nice to have
• music - must be upbeat but not over the top
Should not have
• be too busy on each page

```html
<!DOCTYPE html>
<html lang="en">
<head>
<meta charset="utf-8">
<title>BrixRentals</title>
<link rel="stylesheet" href="https://fonts.googleapis.com/css2?family=Yanone+Kaffeesatz:wght@300;400&family=Pontano+Sans&display=swap">
<style>
  :root {
    --teal: #008b93;
    --ink: #021717;
    --sky: #0fbcd6;
    --sky-edge: #7fe2f0;
    --slate: #5a524e;
    --white: #ffffff;
    --copy: #e6eeee;
    --brand-tile: #3a2f31;
  }
  * { box-sizing: border-box; margin: 0; padding: 0; }
  html, body { width: 1200px; height: 695px; overflow: hidden; }
  body {
    position: relative;
    background: var(--teal);
    font-family: Arial, Helvetica, sans-serif;
    color: var(--copy);
  }
  .ground {
    position: absolute; left: 0; top: 557px; width: 1200px; height: 138px;
    background: var(--ink);
  }
  .ground-accent { position: absolute; left: 0; top: 0; width: 1200px; height: 695px; }
  .page-column {
    position: absolute; left: 156px; top: 600px; width: 892px; height: 95px;
    background: var(--teal);
  }
  .page {
    position: absolute; left: 156px; top: 43px; width: 892px; height: 573px;
    background: var(--ink); border-radius: 9px;
  }
  .brand {
    position: absolute; left: 38px; top: 22px;
    display: flex; align-items: center; gap: 10px;
  }
  .brand-mark { width: 22px; height: 22px; background: var(--brand-tile); }
  .brand-name {
    font-family: "Pontano Sans", sans-serif; font-size: 26px; color: var(--white);
  }
  .tagline {
    position: absolute; left: 35px; top: 104px;
    font-family: "Pontano Sans", sans-serif; font-size: 16px; color: var(--white);
  }
  .main-nav {
    position: absolute; left: 30px; top: 129px; width: 832px; height: 41px;
    background: var(--sky); border: 1px solid var(--sky-edge); border-radius: 8px;
    display: flex; justify-content: flex-end; align-items: center; padding-right: 10px;
  }
  .main-nav a {
    font-family: "Yanone Kaffeesatz", sans-serif; font-weight: 300; font-size: 19px;
    color: var(--white); text-decoration: none; margin-left: 37px;
  }
  .intro-art {
    position: absolute; left: 34px; top: 193px; width: 78px; height: 72px;
    background: linear-gradient(135deg, #f2f2f2 0%, #d8d8d8 55%, #e6c24a 100%);
    transform: skewY(-8deg);
  }
  .welcome-title {
    position: absolute; left: 125px; top: 240px;
    font-family: "Pontano Sans", sans-serif; font-weight: 400; font-size: 28px; color: var(--white);
  }
  .body-copy { position: absolute; font-size: 13px; line-height: 16px; }
  .footer-bar {
    position: absolute; left: 30px; top: 496px; width: 832px; height: 50px;
    background: var(--sky); border: 1px solid var(--sky-edge); border-radius: 8px;
    display: flex; justify-content: center; align-items: center;
    font-family: "Yanone Kaffeesatz", sans-serif; font-weight: 300; font-size: 19px; color: var(--white);
  }
</style>
</head>
<body>
  <div class="ground"></div>
  <svg class="ground-accent" viewBox="0 0 1200 695" aria-hidden="true">
    <polygon points="1097,557 1200,486 1200,557" fill="var(--slate)"/>
  </svg>
  <div class="page-column"></div>

  <main class="page">
    <div class="brand">
      <span class="brand-mark"></span>
      <span class="brand-name">BRIX Rentals</span>
    </div>
    <p class="tagline">"good quality, outstanding service and attention to detail, energetic, integrity, "</p>

    <nav class="main-nav">
      <a href="#">Home</a>
      <a href="#">Profile</a>
      <a href="#">Services</a>
      <a href="#">Owner info</a>
      <a href="#">Tenant info</a>
      <a href="#">Properties</a>
      <a href="#">Darwin</a>
    </nav>

    <div class="intro-art" role="img" aria-label="Illustration of paper documents with a pencil and paper clip"></div>
    <h1 class="welcome-title">Welcome to the BrixRentals</h1>

    <p class="body-copy" style="left:125px; top:305px;">texttttttttttttttttttttttttttttttttttttttttttttttttttttttttttttttttt</p>
    <p class="body-copy" style="left:31px; top:352px;">texttttttttttttttttttttttttttttttttttttttttttttttttttttttttttttttttt</p>
    <p class="body-copy" style="left:31px; top:393px;">texttttttttttttttttttttttttttttttttttttttttttttttttttttttttttttttttt</p>
    <p class="body-copy" style="left:31px; top:434px;">texttttttttttttttttttttttttttttttttttttttttttttttttttttttttttttttttt</p>
    <p class="body-copy" style="left:31px; top:475px;">texttttttttttttttttttttttttttttttttttttttttttttttttttttttttttttttttt</p>

    <footer class="footer-bar">Copyright 2015 - BrixRentals</footer>
  </main>
</body>
</html>
```